Brook 4 Brook letterhead design and business card design for electrical company

I need a letterhead that can be used for my invoices and quote books along with emails sent to clients. I have a logo and the logo of Volt Guild I just need all my information placed nicely with a good flow.

Business Name: Brook 4 Brook Electrical
Name: Daniel Karvounis
Abn: 58917204316
Licence Number: 67413
Number: 0400583641

Thank you in advanced

Target Market(s)

Electrical Clients

Industry/Entity Type

Business

Contact Information for Business Card

Name: Daniel Karvounis
Abn: 58917204316
Licence Number: 67413
Number: 0400583641

Font styles to use
Sans Serif

Colors

Designer to choose colors to be used in the design.

Requirements
Must have
• Must have my logo, volt guild logo even if its smaller and in the corner and all details
Nice to have
• Domestic Commercial Industrial stated on there somewhere

```html
<!DOCTYPE html>
<html lang="en">
<head>
<meta charset="utf-8">
<title>Brook 4 Brook Electrical – Letterhead</title>
<link rel="stylesheet" href="https://fonts.googleapis.com/css2?family=Montserrat:wght@500;700;800&family=Roboto+Condensed:wght@400&display=swap">
<style>
  :root {
    --backdrop: #a9cfe9;
    --paper: #ffffff;
    --brand-navy: #1d4394;
    --brand-blue: #2f6fc0;
    --brand-green: #8dc21f;
    --ink: #2b2b2b;
    --ink-muted: #8a8f96;
    --watermark: #f2f3f5;
    --tile: #eef1f8;
    --badge-dark: #1f3550;
  }
  * { margin: 0; padding: 0; box-sizing: border-box; }
  html, body {
    width: 1200px; height: 784px; overflow: hidden;
    background: var(--backdrop);
  }
  .letterhead {
    position: absolute;
    left: 338px; top: 22px;
    width: 523px; height: 740px;
    background: var(--paper);
    box-shadow: 0 6px 18px rgba(30, 70, 120, 0.18);
    overflow: hidden;
  }
  .brand {
    position: absolute; left: 34px; top: 32px;
    font-family: "Montserrat", sans-serif;
  }
  .brand-name {
    display: flex; align-items: center; gap: 7px;
    color: var(--brand-navy);
    font-weight: 800; font-size: 17px; letter-spacing: 0.2px;
    text-transform: uppercase; line-height: 1.05;
  }
  .brand-mark {
    width: 12px; height: 12px; background: var(--brand-navy); flex: none;
  }
  .brand-owner {
    margin-top: 5px; margin-left: 19px;
    color: var(--brand-navy);
    font-weight: 700; font-size: 9.5px;
  }
  .watermark {
    position: absolute; left: 0; right: 0; top: 300px;
    text-align: center;
    font-family: "Montserrat", sans-serif;
    font-weight: 800; font-size: 72px; line-height: 1;
    color: var(--watermark);
    text-transform: uppercase;
  }
  .membership {
    position: absolute; right: 18px; top: 70px;
    width: 120px; height: 110px;
  }
  .membership .tile { position: absolute; background: var(--tile); }
  .membership .tile-a { right: 0; top: 0; width: 40px; height: 40px; }
  .membership .tile-b { right: 22px; top: 28px; width: 52px; height: 52px; opacity: .7; }
  .membership .tile-c { right: 50px; top: 62px; width: 46px; height: 46px; opacity: .6; }
  .member-badge {
    position: absolute; left: 0; top: 30px;
    display: flex; align-items: center; gap: 6px;
    font-family: "Montserrat", sans-serif;
  }
  .member-square {
    width: 26px; height: 26px; background: var(--badge-dark); flex: none;
  }
  .member-name {
    font-weight: 700; font-size: 10px; color: var(--badge-dark);
    text-transform: uppercase; line-height: 1.15;
  }
  .member-name span { display: block; font-weight: 500; color: var(--ink-muted); }
  .contact-line {
    position: absolute; left: 34px; bottom: 24px;
    display: flex; gap: 14px;
    font-family: "Roboto Condensed", sans-serif;
    font-size: 11px; color: var(--ink);
  }
  .contact-item { display: flex; align-items: center; gap: 5px; }
  .contact-item svg { flex: none; }
  .footer-band {
    position: absolute; left: 0; right: 0; bottom: 0; height: 9px;
    display: flex;
  }
  .footer-band .band-blue {
    flex: 0 0 66%;
    background: linear-gradient(90deg, var(--brand-blue), var(--brand-navy));
  }
  .footer-band .band-green { flex: 1; background: var(--brand-green); margin-left: 4px; }
</style>
</head>
<body>
  <main class="letterhead">
    <header class="brand">
      <div class="brand-name"><span class="brand-mark"></span>Brook 4 Brook Electrical</div>
      <div class="brand-owner">Daniel Karvounis</div>
    </header>

    <div class="membership">
      <span class="tile tile-a"></span>
      <span class="tile tile-b"></span>
      <span class="tile tile-c"></span>
      <div class="member-badge">
        <span class="member-square"></span>
        <div class="member-name">Volt Guild<span>Member</span></div>
      </div>
    </div>

    <div class="watermark" aria-hidden="true">Brook 4 Brook</div>

    <footer class="contact-line">
      <div class="contact-item">
        <svg width="7" height="7" viewBox="0 0 7 7"><circle cx="3.5" cy="3.5" r="3" fill="none" stroke="#2f6fc0"/><circle cx="3.5" cy="3.5" r="1.4" fill="#2f6fc0"/></svg>
        Abn: 58917204316
      </div>
      <div class="contact-item">
        <svg width="7" height="7" viewBox="0 0 7 7"><circle cx="3.5" cy="3.5" r="3" fill="none" stroke="#2f6fc0"/><circle cx="3.5" cy="3.5" r="1.4" fill="#2f6fc0"/></svg>
        Licence Number: 67413
      </div>
      <div class="contact-item">
        <svg width="7" height="7" viewBox="0 0 7 7"><circle cx="3.5" cy="3.5" r="3" fill="none" stroke="#2f6fc0"/><circle cx="3.5" cy="3.5" r="1.4" fill="#2f6fc0"/></svg>
        Number: 0400583641
      </div>
    </footer>
    <div class="footer-band"><span class="band-blue"></span><span class="band-green"></span></div>
  </main>
</body>
</html>
```